Amber Lantern Cafe Business Card

We need a business card design for a new European Cafe. Main menu will be coffee and deserts.

Requirements
Must have
• Logo - 1 of the attached versions
Address - TBA (you can use 487 Morrow Ave Unit 9 for now)
Phone - TBA (you can use 555-238-4176 for now)

```html
<!DOCTYPE html>
<html lang="en">
<head>
<meta charset="utf-8">
<title>Amber Lantern Cafe – Business Card</title>
<link rel="stylesheet" href="https://fonts.googleapis.com/css2?family=Open+Sans:wght@400;600&family=PT+Sans+Narrow:wght@400&display=swap">
<style>
  :root{
    --page:#ece7e1;
    --red-deep:#9b0b12;
    --red-warm:#b03b2d;
    --cream:#f8efe0;
    --cream-text:#fbf4ea;
    --label:#555;
    --shadow:rgba(0,0,0,.28);
  }
  *{margin:0;padding:0;box-sizing:border-box}
  html,body{width:1200px;height:1000px;overflow:hidden;background:var(--page)}
  .canvas{position:relative;width:1200px;height:1000px}

  .card{position:absolute;left:274px;width:652px;height:360px;overflow:hidden;
        box-shadow:0 4px 10px var(--shadow)}
  .card--front{top:68px;background:var(--red-deep)}
  .card--back{top:548px;background:var(--red-warm)}
  .card__bg{position:absolute;inset:0;width:100%;height:100%}

  .card__label{position:absolute;left:0;width:100%;text-align:center;
        font:italic 400 17px/1 "PT Sans Narrow",sans-serif;letter-spacing:2px;color:var(--label)}
  .label--front{top:462px}
  .label--back{top:936px}

  /* front brand lockup */
  .brand{position:absolute;left:132px;top:127px;display:flex;align-items:center}
  .brand__mark{width:98px;height:98px;border-radius:6px;background:var(--cream);flex:none}
  .brand__name{margin-left:20px;font:600 36px/1.12 "Open Sans",sans-serif;color:var(--cream-text);
               text-align:center;white-space:nowrap}

  /* back */
  .panel{position:absolute;left:48px;top:0;width:227px;height:306px;background:var(--cream);
         border-radius:0 0 14px 14px;text-align:center}
  .panel__mark{width:58px;height:58px;border-radius:4px;background:var(--red-deep);margin:135px auto 0}
  .panel__name{font:600 20px/1.15 "Open Sans",sans-serif;color:var(--red-deep);margin-top:12px}

  .contact{position:absolute;left:322px;top:108px;color:var(--cream-text);
           font:400 17px/1.3 "PT Sans Narrow",sans-serif}
  .contact__name{font-size:33px;line-height:1;margin-bottom:22px}
  .contact__row{display:flex;align-items:flex-start;margin-bottom:17px}
  .contact__icon{width:22px;height:22px;margin-right:13px;flex:none;fill:var(--cream-text)}

  .web{position:absolute;left:70px;top:323px;display:flex;align-items:center;color:var(--cream-text);
       font:400 15px/1 "Open Sans",sans-serif}
  .web svg{width:24px;height:24px;margin-right:8px}
</style>
</head>
<body>
<main class="canvas">

  <section class="card card--front" aria-label="Card front">
    <svg class="card__bg" viewBox="0 0 652 360" aria-hidden="true">
      <polygon points="62,0 652,0 652,360 187,360" fill="var(--red-warm)"/>
    </svg>
    <svg class="card__bg" viewBox="0 0 652 360" role="img" aria-label="Large decorative swirl pattern area">
      <defs>
        <radialGradient id="swirlFront" cx="0.5" cy="0.5" r="0.5">
          <stop offset="0" stop-color="var(--red-deep)" stop-opacity=".75"/>
          <stop offset="1" stop-color="var(--red-deep)" stop-opacity="0"/>
        </radialGradient>
      </defs>
      <ellipse cx="480" cy="170" rx="230" ry="210" fill="url(#swirlFront)"/>
    </svg>
    <div class="brand">
      <div class="brand__mark"></div>
      <p class="brand__name">Amber Lantern<br>Cafe</p>
    </div>
  </section>
  <p class="card__label label--front">FRONT</p>

  <section class="card card--back" aria-label="Card back">
    <svg class="card__bg" viewBox="0 0 652 360" role="img" aria-label="Decorative swirl pattern area">
      <defs>
        <radialGradient id="swirlBack" cx="0.5" cy="0.5" r="0.5">
          <stop offset="0" stop-color="var(--red-deep)" stop-opacity=".6"/>
          <stop offset="1" stop-color="var(--red-deep)" stop-opacity="0"/>
        </radialGradient>
      </defs>
      <ellipse cx="440" cy="150" rx="240" ry="220" fill="url(#swirlBack)"/>
      <polygon points="600,0 652,0 652,120" fill="var(--red-deep)"/>
    </svg>
    <div class="panel">
      <div class="panel__mark"></div>
      <p class="panel__name">Amber Lantern<br>Cafe</p>
    </div>
    <div class="contact">
      <p class="contact__name">John Doe</p>
      <div class="contact__row">
        <svg class="contact__icon" viewBox="0 0 24 24" aria-hidden="true"><path d="M8 2h8a2 2 0 0 1 2 2v16a2 2 0 0 1-2 2H8a2 2 0 0 1-2-2V4a2 2 0 0 1 2-2zm0 3v7h8V5zm1 9v2h2v-2zm4 0v2h2v-2zm-4 3v2h2v-2zm4 0v2h2v-2z"/></svg>
        <span>555-238-4176</span>
      </div>
      <div class="contact__row">
        <svg class="contact__icon" viewBox="0 0 24 24" aria-hidden="true"><path d="M12 1a8 8 0 0 0-8 8c0 6 8 14 8 14s8-8 8-14a8 8 0 0 0-8-8zm0 11a3 3 0 1 1 0-6 3 3 0 0 1 0 6z"/></svg>
        <span>N. 44d 03.12 W. 23.05.40</span>
      </div>
      <div class="contact__row">
        <svg class="contact__icon" viewBox="0 0 24 24" aria-hidden="true"><path d="M12 2 1 12h3v10h6v-6h4v6h6V12h3z"/></svg>
        <span>487 Morrow Ave Unit 9<br>Larkfield, Oregon, United States, 97402</span>
      </div>
    </div>
    <div class="web">
      <svg viewBox="0 0 24 24" aria-hidden="true" fill="none" stroke="var(--cream-text)" stroke-width="1.6"><circle cx="12" cy="12" r="10"/><ellipse cx="12" cy="12" rx="4.5" ry="10"/><path d="M2 12h20M4 7h16M4 17h16"/></svg>
      <span>www.yourcompany.com</span>
    </div>
  </section>
  <p class="card__label label--back">BACK</p>

</main>
</body>
</html>
```